Business card design needed

We do excavation, cartage and contracting
I would quote like to have a picture of my digger as the whole back ground and the words on top. If that looks any good
Otherwise please feel free to come up with any other cool options

Cheers Marc

KLR Contracting
Excavation, Cartage, Contracting
Marcus Prewitt
www.klr-example.co.nz
021 584 067
marc@klr-example.co.nz

```html
<!DOCTYPE html>
<html lang="en">
<head>
<meta charset="utf-8">
<title>KLR Contracting – Business Card</title>
<link rel="stylesheet" href="https://fonts.googleapis.com/css2?family=Cinzel:wght@400;500&display=swap">
<style>
  :root {
    --backdrop-light: #f7f7f7;
    --backdrop-dark: #d9d9d9;
    --card-yellow: #fbc935;
    --card-yellow-deep: #f3b52a;
    --ink: #1f1a12;
  }
  * { margin: 0; padding: 0; box-sizing: border-box; }
  html, body { width: 1200px; height: 960px; overflow: hidden; }
  body {
    background: radial-gradient(ellipse at 50% 45%, var(--backdrop-light) 35%, var(--backdrop-dark) 100%);
    font-family: "Cinzel", "Times New Roman", serif;
    color: var(--ink);
    position: relative;
  }
  .card {
    position: absolute;
    left: 330px;
    width: 540px;
    height: 310px;
    background: linear-gradient(120deg, var(--card-yellow-deep) 0%, var(--card-yellow) 55%, var(--card-yellow-deep) 100%);
    box-shadow: 0 6px 18px rgba(0,0,0,0.18);
    display: flex;
    flex-direction: column;
    align-items: center;
    justify-content: center;
    text-align: center;
  }
  .card--front { top: 130px; }
  .card--back { top: 520px; }

  .brand-mark {
    display: flex;
    align-items: center;
    gap: 12px;
    margin-bottom: 26px;
  }
  .brand-mark__square {
    width: 26px;
    height: 26px;
    background: var(--ink);
  }
  .brand-mark__name {
    font-size: 44px;
    font-weight: 500;
    letter-spacing: 3px;
  }
  .services {
    font-size: 19px;
    line-height: 1.25;
    letter-spacing: 0.5px;
  }

  .holder-name {
    font-size: 34px;
    font-weight: 400;
    letter-spacing: 1px;
    margin-bottom: 18px;
  }
  .contact-list {
    list-style: none;
    font-size: 15px;
    line-height: 1.35;
    letter-spacing: 0.3px;
  }
</style>
</head>
<body>
  <section class="card card--front" aria-label="Card front">
    <div class="brand-mark">
      <span class="brand-mark__square"></span>
      <span class="brand-mark__name">KLR</span>
    </div>
    <p class="services">KLR Contracting Excavation,<br>Cartage, Contracting</p>
  </section>

  <section class="card card--back" aria-label="Card back">
    <h1 class="holder-name">Marcus Prewitt</h1>
    <ul class="contact-list">
      <li>Website :www.klr-example.co.nz</li>
      <li>Phone Number :021 584 067</li>
      <li>Email Address :marc@klr-example.co.nz</li>
    </ul>
  </section>
</body>
</html>
```